Nordisk Husforum

Company is in: Denmark - Copenhagen
It sells: Restaurants and café buildings
Companys age: 25 years
Main benefit: trust with over 25 years experience

```html
<!DOCTYPE html>
<html lang="da">
<head>
<meta charset="utf-8">
<title>Nordisk Husforum</title>
<link href="https://fonts.googleapis.com/css2?family=Arimo:ital,wght@0,400;0,700;1,400&display=swap" rel="stylesheet">
<style>
:root{
  --page-top:#ffffff;
  --page-bottom:#b9b9b9;
  --ink:#111111;
  --shell:#3d3d3d;
  --nav-top:#5a5a5a;
  --nav-bottom:#2e2e2e;
  --nav-divider:#242424;
  --nav-text:#f2f2f2;
  --panel-grey:#474747;
  --field:#ececec;
  --card-top:#ffffff;
  --card-bottom:#dedede;
  --frame:#cfcfcf;
  --button-top:#d9cbbd;
  --button-bottom:#9c8676;
  --arrow:#2aa2e0;
}
*{box-sizing:border-box;margin:0;padding:0}
html,body{width:1200px;height:842px;overflow:hidden}
body{
  position:relative;
  font-family:"Arimo",Arial,sans-serif;
  color:var(--ink);
  background:linear-gradient(to bottom,var(--page-top) 0%,#f4f4f4 20%,var(--page-bottom) 100%);
}
.abs{position:absolute}

/* header */
.brand{left:326px;top:78px;height:32px;display:flex;align-items:center;gap:10px}
.brand-mark{width:13px;height:13px;background:var(--ink)}
.brand-name{font-size:28px;font-weight:400;line-height:1;color:var(--ink);white-space:nowrap}
.contact{left:888px;top:53px;display:flex;align-items:center;gap:5px}
.contact-icon{width:37px;height:37px;border-radius:6px;background:#000;display:flex;align-items:center;justify-content:center}
.contact-phone{font-size:16px;color:var(--ink)}
.search{left:805px;top:98px;width:240px;height:20px;border:1px solid #b5b5b5;background:linear-gradient(#f7f7f7,#e6e6e6);display:flex;align-items:center;justify-content:space-between;padding:0 4px}
.search-text{font-size:11px;color:#777}

/* shell */
.shell{left:156px;top:150px;width:889px;height:692px;background:var(--shell);box-shadow:0 0 4px rgba(0,0,0,.4)}
.nav{left:156px;top:129px;width:889px;height:34px;border-radius:7px 7px 0 0;background:linear-gradient(var(--nav-top),var(--nav-bottom));border:1px solid #222;display:flex}
.nav a{display:flex;align-items:center;justify-content:center;color:var(--nav-text);text-decoration:none;font-size:16px;border-right:1px solid var(--nav-divider);box-shadow:1px 0 0 #666}
.nav a:last-child{border-right:none;box-shadow:none}

/* banner */
.banner{left:172px;top:170px;width:860px;height:233px;border-radius:8px;overflow:hidden;display:flex;border:1px solid #2a2a2a}
.banner-photo{height:100%}
.photo-a{width:201px;background:linear-gradient(135deg,#2e74d0 0%,#6aa6e6 45%,#c9ced4 70%,#8a96a4 100%)}
.photo-b{width:207px;background:linear-gradient(90deg,#d7d7d7,#f3f3f3 40%,#bdbdbd 70%,#e8e8e8);border-left:1px solid #555}
.photo-c{width:198px;background:linear-gradient(160deg,#6fb4ea 0%,#2a7fd0 40%,#134f9c 80%,#2f8fd6 100%);border-left:1px solid #555}
.login{width:254px;background:var(--panel-grey);border-left:1px solid #2a2a2a;position:relative}
.login-label{position:absolute;left:39px;font-size:16px;color:#f3f3f3;text-shadow:0 1px 1px #000}
.login-field{position:absolute;left:40px;width:172px;height:30px;background:var(--field);border:1px solid #bbb}
.login-button{position:absolute;left:64px;top:169px;width:122px;height:29px}
.login-button .pill{position:absolute;left:12px;top:0;width:110px;height:29px;border-radius:4px;background:linear-gradient(var(--button-top),var(--button-bottom));color:#fff;font-size:15px;font-weight:700;display:flex;align-items:center;justify-content:center;padding-left:10px;text-shadow:0 1px 1px #333;box-shadow:0 3px 4px rgba(0,0,0,.45)}
.login-button svg{position:absolute;left:0;top:2px}

/* content card */
.card{left:172px;top:462px;width:855px;height:360px;border-radius:9px;background:linear-gradient(var(--card-top),var(--card-bottom))}
.card-title{left:181px;top:480px;width:826px;height:32px;border-bottom:1px solid #cfcfcf;background:linear-gradient(#ffffff,#eeeeee);font-style:italic;font-weight:400;font-size:21px;padding:4px 0 0 11px}
.card-text{left:190px;top:528px;font-size:12.4px;line-height:16px;white-space:nowrap}
.card-text p{margin-bottom:12px}
.card-text p.indent{padding-left:1px;margin-bottom:16px}
.card-photo{left:778px;width:229px;border:1px solid var(--frame);background:#fff;padding:3px}
.card-photo div{width:100%;height:100%}
.photo-d{top:518px;height:139px}
.photo-d div{background:linear-gradient(180deg,#8fb3dd 0%,#bcd0e6 35%,#d9d3c6 60%,#8c8578 100%)}
.photo-e{top:664px;height:135px}
.photo-e div{background:linear-gradient(120deg,#3d5f70 0%,#9fb5ba 40%,#f2f1e4 70%,#c8cfc6 100%)}

.footer{left:156px;top:825px;width:889px;text-align:center;font-size:11px;font-weight:700;color:#fff}
</style>
</head>
<body>

<header>
  <div class="abs brand">
    <span class="brand-mark"></span>
    <span class="brand-name">NORDISK HUSFORUM</span>
  </div>
  <div class="abs contact">
    <span class="contact-icon">
      <svg width="22" height="26" viewBox="0 0 22 26"><path d="M6 2 L9 2 L11 8 L8 10 C9 14 11 17 14 19 L16 16 L21 19 L20 23 C18 25 15 25 12 22 C7 18 4 13 3 8 C3 5 4 3 6 2 Z" fill="#fff"/></svg>
    </span>
    <span class="contact-phone">+45 31 20 48 60</span>
  </div>
  <div class="abs search">
    <span class="search-text">Search...</span>
    <svg width="20" height="16" viewBox="0 0 20 16"><circle cx="8" cy="7" r="5" fill="#dbe8f2" stroke="#6b8fb0" stroke-width="1.5"/><line x1="12" y1="10" x2="18" y2="15" stroke="#6b8fb0" stroke-width="2.5" stroke-linecap="round"/></svg>
  </div>
</header>

<div class="abs shell"></div>

<nav class="abs nav">
  <a href="#" style="width:113px">Forside</a>
  <a href="#" style="width:151px">Firmainfo</a>
  <a href="#" style="width:149px">Salgsliste</a>
  <a href="#" style="width:196px">Links/Download</a>
  <a href="#" style="width:161px">Nyhedsbrev</a>
  <a href="#" style="width:117px">Kontakt</a>
</nav>

<section class="abs banner">
  <div class="banner-photo photo-a" role="img" aria-label="Modern glass office buildings against a blue sky"></div>
  <div class="banner-photo photo-b" role="img" aria-label="White spiral atrium inside a modern building"></div>
  <div class="banner-photo photo-c" role="img" aria-label="Blue glass tower seen from below"></div>
  <form class="login">
    <span class="login-label" style="top:43px">BRUGER:</span>
    <span class="login-field" style="top:61px"></span>
    <span class="login-label" style="top:104px">KODEORD:</span>
    <span class="login-field" style="top:122px"></span>
    <span class="login-button">
      <span class="pill">Login</span>
      <svg width="36" height="26" viewBox="0 0 36 26"><path d="M2 7 L20 7 L20 1 L34 13 L20 25 L20 19 L2 19 Z" fill="var(--arrow)" stroke="#1670a8" stroke-width="1"/></svg>
    </span>
  </form>
</section>

<main>
  <div class="abs card"></div>
  <h1 class="abs card-title">Welcome To Nordisk Husforum</h1>
  <div class="abs card-text">
    <p>NORDISK HUSFORUM har over 25 års erfaring i branchen, det har givet os et grundigt<br>kendskab til branchens mange spidsfindigheder, og vi kan derfor med sikkerhed sige, at De vil være i<br>gode hænder hos NORDISK HUSFORUM, hvad enten De ønsker at sælge eller købe en<br>restaurationsvirksomhed.</p>
    <p class="indent">Lorem Ipsum is simply dummy text of the printing and typesetting industry. Lorem Ipsum has been<br>the industry's standard dummy text ever since the 1500s, when an unknown printer took a galley of<br>type and scrambled it to make a type specimen book. It has survived not only five centuries, but also<br>the leap into electronic typesetting, remaining essentially unchanged. It was popularised in the 1960s<br>with the release of Arkprint sheets containing Lorem Ipsum passages</p>
    <p class="indent">Lorem Ipsum is simply dummy text of the printing and typesetting industry. Lorem Ipsum has been<br>the industry's standard dummy text ever since the 1500s, when an unknown printer took a galley of<br>type and scrambled it to make a type specimen book. It has survived not only five centuries, but also<br>the leap into electronic typesetting, remaining essentially unchanged. It was popularised in the 1960s<br>with the release of Arkprint sheets containing.</p>
  </div>
  <figure class="abs card-photo photo-d"><div role="img" aria-label="Large concrete office building with bare winter trees"></div></figure>
  <figure class="abs card-photo photo-e"><div role="img" aria-label="Curved glass facade of a modern building in bright light"></div></figure>
</main>

<footer class="abs footer">Copy Right Nordisk Husforum|all right reserved</footer>

</body>
</html>
```